IT services company needs a business card designed

-2 sided business card.-Front is going to be the logo raised (3D floating effect) on a black background. Make the logos spider web shiny silver and keep the spider the same design. -Back needs to have the following information:Doug Farrow, Managing Partner, Cell: 602-488-3179, Website: Kolvantra.com, Email: Doug@Kolvantra.com
Target Market(s)
IT Services
Industry/Entity Type
It Company
Contact Information for Business Card
-2 sided business card.
-Front is going to be the logo raised (3D floating effect) on a black background. Make the logos spider web shiny silver and keep the spider the same design.
-Back needs to have the following information:
Doug Farrow, Managing Partner, Cell: 602-488-3179, Website: Kolvantra.com, Email: Doug@Kolvantra.com
Look and feel

```html
<!DOCTYPE html>
<html lang="en">
<head>
<meta charset="utf-8">
<title>Kolvantra Business Card</title>
<link href="https://fonts.googleapis.com/css2?family=Oswald:wght@500&family=Roboto+Condensed:wght@300;400&display=swap" rel="stylesheet">
<style>
  :root{
    --stage:#2a2a2c;
    --card:#262830;
    --accent:#29a8e0;
    --accent-deep:#1b6f9e;
    --silver:#c9c9cc;
    --text-light:#e4e4e6;
  }
  html,body{margin:0;padding:0;overflow:hidden;}
  body{width:1200px;height:1200px;background:var(--stage);position:relative;}
  .card{
    position:absolute;left:193px;width:880px;height:502px;
    background:var(--card);border-radius:32px;overflow:hidden;
  }
  .card--back{top:34px;}
  .card--front{top:664px;}
  .ornament{position:absolute;top:50px;width:125px;height:430px;}
  .ornament--left{left:0;background:linear-gradient(90deg,rgba(201,201,204,.18),rgba(201,201,204,.03));border-radius:0 70px 70px 0;}
  .ornament--right{right:0;background:linear-gradient(270deg,rgba(201,201,204,.18),rgba(201,201,204,.03));border-radius:70px 0 0 70px;}
  .emblem{
    position:absolute;left:50%;border-radius:50%;
    background:radial-gradient(circle at 50% 45%,var(--accent) 0%,var(--accent-deep) 38%,rgba(201,201,204,.35) 40%,rgba(201,201,204,.12) 100%);
  }
  .card--back .emblem{top:48px;width:118px;height:118px;margin-left:-59px;}
  .card--front .emblem{top:90px;width:240px;height:240px;margin-left:-120px;}
  .wordmark{
    position:absolute;left:0;right:0;text-align:center;margin:0;line-height:1;
    font-family:"Roboto Condensed",sans-serif;font-weight:400;color:var(--silver);letter-spacing:.04em;
  }
  .card--back .wordmark{top:176px;font-size:34px;}
  .card--front .wordmark{top:360px;font-size:64px;}
  .holder-name{
    position:absolute;top:234px;left:0;right:0;text-align:center;margin:0;
    font-family:"Oswald",sans-serif;font-weight:500;font-size:50px;line-height:1;
    color:var(--accent);letter-spacing:-.02em;text-transform:uppercase;
  }
  .holder-role{
    position:absolute;top:286px;left:0;right:0;text-align:center;margin:0;line-height:1.2;
    font-family:"Roboto Condensed",sans-serif;font-weight:300;font-size:21px;color:var(--text-light);
  }
  .contact-icons{position:absolute;top:340px;left:0;right:0;display:flex;justify-content:center;gap:14px;}
  .contact-icons svg{width:20px;height:20px;}
  .contact-list{
    position:absolute;top:374px;left:0;right:0;margin:0;padding:0;list-style:none;text-align:center;
    font-family:"Roboto Condensed",sans-serif;font-weight:300;font-size:21px;line-height:27px;color:var(--text-light);
  }
</style>
</head>
<body>
  <section class="card card--back">
    <div class="ornament ornament--left" role="img" aria-label="Silver web corner ornament"></div>
    <div class="ornament ornament--right" role="img" aria-label="Silver web corner ornament"></div>
    <span class="emblem" role="img" aria-label="Company emblem area"></span>
    <p class="wordmark">KOLVANTRA</p>
    <h1 class="holder-name">Doug Farrow</h1>
    <p class="holder-role">Managing Partner</p>
    <div class="contact-icons">
      <svg viewBox="0 0 24 24" aria-hidden="true"><path fill="var(--accent)" d="M6.6 10.8a15.1 15.1 0 0 0 6.6 6.6l2.2-2.2c.3-.3.7-.4 1-.2 1.1.4 2.3.6 3.6.6.6 0 1 .4 1 1V20c0 .6-.4 1-1 1A17 17 0 0 1 3 4c0-.6.4-1 1-1h3.5c.6 0 1 .4 1 1 0 1.3.2 2.5.6 3.6.1.3 0 .7-.2 1z"/></svg>
      <svg viewBox="0 0 24 24" aria-hidden="true"><rect x="2" y="5" width="20" height="14" fill="var(--accent)"/><path d="M2 5l10 8 10-8M2 19l7-7M22 19l-7-7" stroke="var(--card)" stroke-width="1.5" fill="none"/></svg>
      <svg viewBox="0 0 24 24" aria-hidden="true"><g fill="none" stroke="var(--accent)" stroke-width="1.6"><circle cx="12" cy="12" r="9"/><ellipse cx="12" cy="12" rx="4" ry="9"/><path d="M3 12h18M5 7h14M5 17h14"/></g></svg>
    </div>
    <ul class="contact-list">
      <li>602-488-3179</li>
      <li>Doug@Kolvantra.com</li>
      <li>www.kolvantra.com</li>
    </ul>
  </section>

  <section class="card card--front">
    <div class="ornament ornament--left" role="img" aria-label="Silver web corner ornament"></div>
    <div class="ornament ornament--right" role="img" aria-label="Silver web corner ornament"></div>
    <span class="emblem" role="img" aria-label="Company emblem area, raised silver finish"></span>
    <p class="wordmark">KOLVANTRA</p>
  </section>
</body>
</html>
```